Wordpress Design Project

WHO WE ARE:
Bright Path Media Group is not just another SEO or PPC company. We work with our clients to help them grow their business and achieve their goals. Our commitment to doing what is best for the customer, is why we have grown so quickly. We believe our business is not about advertising BUT about connecting customers & growing our clients businesses. We see our product as helping people, not selling a product.

PROJECT OVERVIEW:
I need to create a wordpress website for my business, www.brightpathmediagroup.com.au

I need a whole new site created showing all of my services. The services include:
NOTE: These are not the main focus of the home page.

Consulting & Strategy Planning
Search Engine Optimisation
Pay Per Click
Re-Marketing

Once I have selected the top home page design, I will need a product and blog page designed.

SITE DESIGN:
If I was to explain the kind of style I am looking for, it would be high-street, New York agency look, web 2.0. Clean, elegant, stylish, high quality and simple looking. Kind of like you would expect from an plumtree website.

Think of car advertising, the closest to the target market & look/feel Im looking for would be Ferrandell, Korva, Mirel, Talvance, Brisk.

However, I am open to any design style.

DO NOT let this restrict your creativity BUT here are some websites I like the look of.

Home page:
http://www.layoutharbor.example/demo/52816.html
https://www.quorvix.example/intl/en/vantel/devices/
http://www.quorvix.example/intl/en/vantel/devices/features-different.html
http://www.layoutharbor.example/demo/63924.html
https://www.quorvix.example/intl/en/vantel/browser/features.html

Product Page:
http://www.quorvix.example/intl/en/vantel/devices/buynow.html#instore

NOTE: I just added a file called "I like this color scheme.png" you can play around with something like this as well.

Please do not use the content from my current website. That is for a PPC service, the new site is for an full service agency.

Also, the message/tagline is the feature or most prominent element of the website..... Not the services we offer, these are secondary.

Great designs so far everyone, but I think I'm looking a little simpler and less crowded.  Closer to the sample sites I sent.... keep em coming.

Also, I would prefer that the 4 services, do not visually over power the tag line.  The 4 services are not important to the home page.

Lets make this easy, since every design I receive is almost the same...

Make the design look something like these 2 websites.
https://www.quorvix.example/intl/en/vantel/browser/features.html#simplicity

Target Market(s)

Business Owners and entreprenuers who are well established, typically in the 35-60 year old range and spend 100k-1m in advertising per year. They big brands that target these people are Ferrandell, Korva, Mirel, Talvance, Brisk, this should give you the feel for what I am after.

Industry/Entity Type

Advertising

Requirements
Must have
• 1. Navigations: Home, Services, About Us, Blog, Contact Us

2. The main home page words should be.... "We Grow Your Business Online" and "Clear Aim, Clear Plan, Clear Team, Bright Path Media Group" (should use logo for last one)
I would like to see this tagline somewhere in the site "We Don't Want to be the Biggest, Just the Best!"

3. Product page must have a contact form with (name, email, phone, website)
This form must show an offer of "Free Strategy Sessions, Double your website leads", I have included an image to show as an example for the lead form "lead form example.png", see attached.

Nice to have
• I would like to see 1 or 2 of these idea's in the design.

1. I have attached some logos for Promiq & Metrisq certifications + Web association logo you can use for design purposes.

2. You can put company logo's in the design and I can change them to my clients logos at a later date.

3. Testimonials

4. Since our business is about people, pictures of people like business owners, customers using technology such as an slato, or anything like that would be good. However, is not necessary. Some idea: http://www.netmeshly.example/advertising
Should not have
• There will be no video on the design.

```html
<!DOCTYPE html>
<html lang="en">
<head>
<meta charset="utf-8">
<title>Bright Path Media Group</title>
<link rel="stylesheet" href="https://fonts.googleapis.com/css2?family=Noto+Serif&family=Arimo&family=Ubuntu+Condensed&family=Ubuntu:wght@500&display=swap">
<style>
:root{
  --blue-light:#5ea3e8;
  --blue:#3b82d2;
  --blue-dark:#2465b4;
  --navy:#0a3a78;
  --navy-deep:#08356f;
  --title-blue:#2566b3;
  --text:#3a3a3a;
  --band:#ecebeb;
  --white:#ffffff;
  --red:#c8231c;
}
*{box-sizing:border-box;margin:0;padding:0}
html,body{width:1009px;height:1200px;overflow:hidden;background:var(--white)}
body{position:relative;font-family:"Arimo",Arial,sans-serif;color:var(--text)}
.abs{position:absolute}

/* header */
.brand{left:159px;top:26px;display:flex;align-items:center;gap:12px}
.brand-dot{width:30px;height:30px;border-radius:50%;background:var(--blue-dark)}
.brand-name{font-family:"Noto Serif",serif;font-size:22px;color:var(--navy)}
.nav-area{left:494px;top:9px;width:515px;height:80px;background:linear-gradient(90deg,var(--blue),var(--blue-dark));border-top-left-radius:28px}
.nav{left:533px;top:0;display:flex;font-family:"Noto Serif",serif;font-size:12.5px;color:#e8f1fb}
.nav a{color:inherit;text-decoration:none;position:absolute;top:39px;white-space:nowrap}
.nav .home{left:0;top:4px;width:52px;height:77px;border-top:5px solid var(--navy);background:linear-gradient(#5fa7ee,#d9ebfb);color:var(--navy);text-align:center;padding-top:35px}
.hero{left:0;top:83px;width:1009px;height:400px;background:linear-gradient(90deg,var(--blue-light),var(--blue) 55%,var(--blue-dark))}
.slide{left:129px;top:107px;width:762px;height:337px;background:linear-gradient(120deg,#f4f4f4,#d8dadc 55%,#aeb6bf);box-shadow:0 12px 18px -10px rgba(0,0,0,.45)}
.headline{left:149px;top:180px;font-family:"Noto Serif",serif;font-size:31px;font-weight:700;color:#fff;letter-spacing:.5px;text-shadow:0 0 1px #333,1px 1px 0 #555,2px 3px 4px rgba(0,0,0,.45)}
.tagline{left:188px;top:221px;font-family:"Noto Serif",serif;font-size:17px;color:var(--navy)}
.dots{left:471px;top:457px;display:flex;gap:4px}
.dots span{width:17px;height:17px;border-radius:50%;background:#8c8c8c;box-shadow:inset 0 1px 2px rgba(0,0,0,.4)}
.dots span:first-child{background:#fff}

/* services */
.services{left:0;top:483px;width:1009px;height:209px;background:var(--band)}
.service{position:absolute;top:30px;width:176px}
.service-head{display:flex;gap:8px;align-items:flex-start;height:42px}
.service-head svg{flex:none;margin-top:2px}
.service-title{font-family:"Noto Serif",serif;font-size:14.5px;line-height:15.5px;color:var(--title-blue)}
.service p{font-size:12.5px;line-height:15.5px;text-align:justify;margin-top:10px;padding-left:3px}
.more{position:absolute;width:53px;height:22px;background:#fff;border-radius:3px;box-shadow:0 1px 3px rgba(0,0,0,.3);font-size:11.5px;text-align:center;line-height:22px;color:#555}

/* welcome */
.welcome-title{left:131px;top:704px;font-family:"Noto Serif",serif;font-size:21px;color:var(--title-blue)}
.media{left:129px;top:747px;width:259px;height:164px;border:3px solid #222;background:linear-gradient(#d7d7d7,#8b8b8b)}
.copy{font-size:12.5px;line-height:15.5px;text-align:justify}
.copy-right{left:407px;top:743px;width:261px}
.copy-right p+p{margin-top:15px}
.copy-bottom{left:130px;top:920px;width:534px;text-align:left}

/* quote form */
.quote{left:696px;top:704px;width:182px;height:325px;background:linear-gradient(#fff 70%,#e9e9e9);clip-path:polygon(0 0,100% 0,100% 95%,50% 100%,0 95%);box-shadow:0 0 4px rgba(0,0,0,.2)}
.quote-head{position:absolute;left:0;top:0;width:182px;height:58px;background:linear-gradient(#3ea4e4,#1779c4);clip-path:polygon(0 0,100% 0,100% 72%,50% 100%,0 72%);font-family:"Ubuntu Condensed",sans-serif;color:#fff;text-align:center;font-size:18px;line-height:17px;padding-top:10px}
.quote-note{position:absolute;top:66px;width:100%;text-align:center;font-size:7.5px;font-weight:700;color:#222}
.field{position:absolute;left:12px;width:159px;height:23px;border:1px solid #c9c9c9;border-radius:2px;background:#fff;box-shadow:inset 0 1px 2px rgba(0,0,0,.1);font-size:6.5px;color:#888;padding:7px 8px}
.field svg{position:absolute;right:4px;top:6px}
.submit{position:absolute;left:39px;top:272px;width:105px;height:25px;border-radius:3px;background:linear-gradient(#e0372d,#a91710);color:#fff;font-family:"Ubuntu",sans-serif;font-weight:500;font-size:11.5px;text-align:center;line-height:25px}

/* footer */
.footer{left:0;top:1050px;width:1009px;height:150px;background:var(--navy-deep)}
.footer-links{left:0;top:1066px;width:1009px;text-align:center;font-family:"Ubuntu Condensed",sans-serif;font-size:12px;color:#fff;letter-spacing:.4px;word-spacing:2px}
.rule{left:20px;width:969px;height:1px;background:linear-gradient(90deg,transparent,#3c6aa6,transparent)}
.follow{left:440px;top:1112px;display:flex;align-items:center;gap:10px;font-family:"Ubuntu",sans-serif;font-weight:500;font-size:10px;color:#fff}
.follow i{display:block;width:23px;height:23px;border:2px solid #fff;border-radius:50%}
.copyright{left:0;top:1160px;width:1009px;text-align:center;font-family:"Ubuntu Condensed",sans-serif;font-size:12px;color:#fff}
</style>
</head>
<body>
<header>
  <div class="abs brand"><span class="brand-dot"></span><span class="brand-name">Bright Path Media Group</span></div>
  <div class="abs nav-area"></div>
  <nav class="abs nav">
    <a class="home" href="#">Home</a>
    <a href="#" style="left:72px">Services</a>
    <a href="#" style="left:149px">About Us</a>
    <a href="#" style="left:230px">Blog</a>
    <a href="#" style="left:286px">Contact Us</a>
  </nav>
</header>

<section>
  <div class="abs hero"></div>
  <div class="abs slide" role="img" aria-label="Photo of a confident businessman in a white hard hat with arms crossed, power lines under an overcast sky"></div>
  <h1 class="abs headline">We Grow Your Business Online</h1>
  <p class="abs tagline">We Don't Want to be the Biggest, Just the Best !</p>
  <div class="abs dots"><span></span><span></span><span></span><span></span><span></span></div>
</section>

<section class="abs services">
  <div class="service" style="left:127px">
    <div class="service-head">
      <svg width="28" height="28" viewBox="0 0 28 28" fill="none" stroke="#555" stroke-width="2"><circle cx="14" cy="8" r="5"/><path d="M3 26c0-6 5-10 11-10s11 4 11 10z"/></svg>
      <div class="service-title">Consulting &amp; Strategy Planning</div>
    </div>
    <p>Nullam eget felis id metus luctus semper quis vel nulla. Cras diam mauris, molestie eu sodales non,</p>
  </div>
  <div class="service" style="left:323px">
    <div class="service-head">
      <svg width="28" height="28" viewBox="0 0 28 28" fill="none" stroke="#555" stroke-width="2.4"><circle cx="16" cy="11" r="8"/><path d="M10 17L3 25"/></svg>
      <div class="service-title">Search Engine Optimisation</div>
    </div>
    <p>Nullam eget felis id metus luctus semper quis vel nulla. Cras diam mauris, molestie eu sodales non,</p>
  </div>
  <div class="service" style="left:523px">
    <div class="service-head">
      <svg width="28" height="28" viewBox="0 0 28 28" fill="none" stroke="#555" stroke-width="2.4"><rect x="3" y="6" width="19" height="19" rx="3"/><path d="M8 14l5 5L26 4"/></svg>
      <div class="service-title" style="padding-top:3px">Pay Per Click</div>
    </div>
    <p>Nullam eget felis id metus luctus semper quis vel nulla. Cras diam mauris, molestie eu sodales non,</p>
  </div>
  <div class="service" style="left:717px">
    <div class="service-head">
      <svg width="28" height="28" viewBox="0 0 28 28"><rect x="2" y="3" width="24" height="22" rx="6" fill="none" stroke="#555" stroke-width="2.4"/><rect x="8" y="9" width="6" height="6" fill="#555"/><rect x="14" y="14" width="6" height="6" fill="#555"/></svg>
      <div class="service-title" style="padding-top:3px">Re-Marketing</div>
    </div>
    <p>Nullam eget felis id metus luctus semper quis vel nulla. Cras diam mauris, molestie eu sodales non,</p>
  </div>
  <span class="more" style="left:255px;top:155px">more..</span>
  <span class="more" style="left:448px;top:155px">more..</span>
  <span class="more" style="left:641px;top:155px">more..</span>
  <span class="more" style="left:840px;top:155px">more..</span>
</section>

<main>
  <h2 class="abs welcome-title">Welcome to Bright Path Media Group</h2>
  <div class="abs media" role="img" aria-label="Promotional still with bold lettering about increasing online advertising return"></div>
  <div class="abs copy copy-right">
    <p>Nulla libero ipsum, scelerisque in suscipit eu, faucibus id nulla. Morbi eu nisl enim. Phasellus vehicula commodo massa eget ornare. Donec sit ametNulla libero ipsum, scelerisque in suscipit eu, faucibus id nulla. Morbi eu nisl enim. Phasellus vehicula commodo massa eget ornare. Donec sit amet.</p>
    <p>Nulla libero ipsum, scelerisque in suscipit eu, faucibus id nulla commodo massa eget ornare. Donec sit amet.</p>
  </div>
  <p class="abs copy copy-bottom">Aenean placerat tortor ac dui luctus ut mattis est mollis. Donec blandit orci id velit cursus varius. Fusce quam enim, hendrerit nec ultrices a, vestibulum nec enim. Quisque imperdiet ultricies dolor in convallis. Morbi sed fringilla elit.Aenean placerat tortor ac dui luctus ut mattis est mollis. Donec blandit orci id velit cursus varius. Fusce quam enim, hendrerit nec ultrices a, vestibulum nec enim.</p>
  <span class="more" style="left:610px;top:1006px">more..</span>

  <aside class="abs quote">
    <div class="quote-head">GET A QUOTATION<br>FOR FREE!</div>
    <div class="quote-note">Please select a service from below</div>
    <div class="field" style="top:78px">Social Bookmarking Services<svg width="10" height="10" viewBox="0 0 10 10"><rect width="10" height="10" fill="#6a8fc8"/><path d="M2 4l3 3 3-3" stroke="#fff" fill="none"/></svg></div>
    <div class="field" style="top:109px">Name</div>
    <div class="field" style="top:141px">Email</div>
    <div class="field" style="top:173px">Website</div>
    <div class="field" style="top:204px;height:59px">Message</div>
    <div class="submit">SUBMIT NOW !</div>
  </aside>
</main>

<footer>
  <div class="abs footer"></div>
  <div class="abs footer-links">HOME &nbsp;|&nbsp; COMPANY &nbsp;|&nbsp; SERVICES &nbsp;|&nbsp; SOLUTIONS &nbsp;|&nbsp; RESOURCE CENTER &nbsp;|&nbsp; PARTNERS &nbsp;|&nbsp; SUPPORT &nbsp;|&nbsp; PRIVACY POLICY &nbsp;|&nbsp; SITEMAP</div>
  <div class="abs rule" style="top:1099px"></div>
  <div class="abs follow">FOLLOW US : <i></i><i></i></div>
  <div class="abs rule" style="top:1149px"></div>
  <div class="abs copyright">COPYRIGHT © 2013 BRIGHT PATH MEDIA GROUP. ALL RIGHTS RESERVED.</div>
</footer>
</body>
</html>
```